Frame Design for a collection of Tarot Cards

Update 1: I've added a drawing showing a corner of the framed collection. Note that the name of the character depicted on the tarot card is included below the card and not on the card itself. There will also be some space to include a few of lines of text about the person shown on the card.
Update 2: While it will be nice to see some examples of tarot cards contained within the frame, we are not expecting you to design cards at this stage.
-----------------------------
We need some graphic designs for framed collections of tarot cards.
The frames will be quite retro - probably looking like wood that has a distressed paint finish.
All the cards, except one, will be normal sized tarot cards that, in the finished product, will be back lit. One card will be extra large (see rough sketch) and will also be back lit.
Above the large central tarot card will be a screen that in default mode will show the back of a tarot card.
Beneath the large tarot card will be a circular recess that will display one of the platonic solids. In this design it will contain a dodecahedron.
Please note that we will be producing other picture frames containing 4, 6, 8, and 20 of the smaller tarot cards.
The cards will all be under glass that is held in place by the frame.
The keyhole will also be under the glass.
Ultimately, we will be producing 30 of these framed tarot card collections.
The tarot cards will be bespoke, that is to say they will look like old fashioned tarot cards, but they will depict people associated with the city of Cambridge (such as Walter Fenwick, Gordon Millbray, Lou Kimble et al).
The graphic design will be used within a presentation pack to illustrate the look and feel of a new bar that is under construction in Cambridge, UK. The idea is to create a basement gallery that is also a cocktail bar.
We welcome ideas for how the mount board for the cards should look.
At this stage we recommend showing us some sample ideas of how you think the framed collection might look. If we think you are on the right track, we will let you know. We don't want you putting in a lot of work that might not come to anything.
Once we have a design that we think is on the right track, we will increase the budget for the project by at least £100.

```html
<!DOCTYPE html>
<html lang="en">
<head>
<meta charset="utf-8">
<title>Tarot Collection Frame</title>
<style>
  :root {
    --page: #f9f7f3;
    --frame-dark: #2e0203;
    --frame-red: #520000;
    --mount: #f9f7f3;
    --card-border: #0f5f70;
    --card-border-shade: #2f3540;
    --recess: #2e0203;
    --solid-line: #ffffff;
  }
  * { margin: 0; padding: 0; box-sizing: border-box; }
  html, body {
    width: 1014px;
    height: 1200px;
    overflow: hidden;
    background: var(--page);
  }
  .canvas {
    position: relative;
    width: 1014px;
    height: 1200px;
    background: var(--page);
  }
  .frame {
    position: absolute;
    left: 98px;
    top: 60px;
    width: 823px;
    height: 1096px;
    background:
      radial-gradient(ellipse 90px 70px at 360px 40px, var(--frame-red) 0%, var(--frame-red) 55%, transparent 80%),
      radial-gradient(ellipse 70px 60px at 120px 60px, var(--frame-red) 0%, var(--frame-red) 45%, transparent 80%),
      radial-gradient(ellipse 55px 130px at 40px 220px, var(--frame-red) 0%, var(--frame-red) 45%, transparent 80%),
      radial-gradient(ellipse 60px 90px at 60px 500px, var(--frame-red) 0%, var(--frame-red) 40%, transparent 80%),
      radial-gradient(ellipse 50px 70px at 45px 920px, var(--frame-red) 0%, var(--frame-red) 45%, transparent 80%),
      radial-gradient(ellipse 60px 110px at 790px 160px, var(--frame-red) 0%, var(--frame-red) 45%, transparent 80%),
      radial-gradient(ellipse 55px 70px at 790px 390px, var(--frame-red) 0%, var(--frame-red) 45%, transparent 80%),
      radial-gradient(ellipse 50px 70px at 795px 960px, var(--frame-red) 0%, var(--frame-red) 40%, transparent 80%),
      radial-gradient(ellipse 90px 55px at 360px 1060px, var(--frame-red) 0%, var(--frame-red) 50%, transparent 80%),
      radial-gradient(ellipse 70px 50px at 120px 1060px, var(--frame-red) 0%, var(--frame-red) 45%, transparent 80%),
      radial-gradient(ellipse 80px 45px at 560px 70px, var(--frame-red) 0%, var(--frame-red) 40%, transparent 80%),
      var(--frame-dark);
  }
  .mount {
    position: absolute;
    left: 164px;
    top: 138px;
    width: 686px;
    height: 942px;
    background: var(--mount);
  }
  .corner-knob {
    position: absolute;
    width: 72px;
    height: 68px;
    border-radius: 50%;
    background: var(--recess);
  }
  .corner-knob--left { left: 178px; top: 160px; }
  .corner-knob--right { left: 766px; top: 160px; }
  .card-slot {
    position: absolute;
    background:
      radial-gradient(circle at 15% 10%, var(--card-border-shade) 0%, transparent 18%),
      radial-gradient(circle at 80% 35%, var(--card-border-shade) 0%, transparent 16%),
      radial-gradient(circle at 10% 70%, var(--card-border-shade) 0%, transparent 15%),
      radial-gradient(circle at 90% 85%, var(--card-border-shade) 0%, transparent 17%),
      radial-gradient(circle at 50% 98%, var(--card-border-shade) 0%, transparent 14%),
      var(--card-border);
  }
  .card-slot::before {
    content: "";
    position: absolute;
    background: var(--mount);
  }
  .card-slot--small { width: 73px; height: 100px; }
  .card-slot--small::before { inset: 6px; }
  .card-slot--screen {
    left: 432px;
    top: 182px;
    width: 152px;
    height: 209px;
  }
  .card-slot--screen::before { inset: 14px 12px; }
  .card-slot--feature {
    left: 385px;
    top: 492px;
    width: 245px;
    height: 317px;
  }
  .card-slot--feature::before { inset: 25px 20px; }
  .column--left .card-slot { left: 238px; }
  .column--right .card-slot { left: 702px; }
  .solid-recess {
    position: absolute;
    left: 445px;
    top: 926px;
    width: 129px;
    height: 121px;
  }
</style>
</head>
<body>
<div class="canvas">
  <div class="frame" role="img" aria-label="Dark red distressed wood frame with swirling ornamental pattern"></div>
  <div class="mount"></div>

  <div class="corner-knob corner-knob--left"></div>
  <div class="corner-knob corner-knob--right"></div>

  <div class="card-slot card-slot--screen" role="img" aria-label="Screen showing the back of a tarot card, framed with teal ornamental border"></div>
  <div class="card-slot card-slot--feature" role="img" aria-label="Large feature tarot card, framed with teal ornamental border"></div>

  <div class="column column--left">
    <div class="card-slot card-slot--small" style="top:258px"></div>
    <div class="card-slot card-slot--small" style="top:388px"></div>
    <div class="card-slot card-slot--small" style="top:519px"></div>
    <div class="card-slot card-slot--small" style="top:649px"></div>
    <div class="card-slot card-slot--small" style="top:779px"></div>
    <div class="card-slot card-slot--small" style="top:909px"></div>
  </div>
  <div class="column column--right">
    <div class="card-slot card-slot--small" style="top:259px"></div>
    <div class="card-slot card-slot--small" style="top:389px"></div>
    <div class="card-slot card-slot--small" style="top:520px"></div>
    <div class="card-slot card-slot--small" style="top:650px"></div>
    <div class="card-slot card-slot--small" style="top:780px"></div>
    <div class="card-slot card-slot--small" style="top:910px"></div>
  </div>

  <svg class="solid-recess" viewBox="0 0 129 121" aria-label="Circular recess holding a dodecahedron">
    <ellipse cx="64.5" cy="60.5" rx="64.5" ry="60.5" fill="var(--recess)"/>
    <polygon points="38,24 88,24 104,74 63,106 22,74"
             fill="none" stroke="var(--solid-line)" stroke-width="2" stroke-linejoin="round"/>
  </svg>
</div>
</body>
</html>
```